L' Breeza Vita, 95% quality oxygen

Task description
L' Breeza Vita, is quality oxygen can for everyone. Our target countries are USA and Europe. Those who exhausted from intense exercises, stress from work, hangover from drinking, or ever those caused by altitude. Therefore, the concept of label must be freshening up after use with elegance and luxury look.
Our can size is as follow.
Diameter: 3.8 cm
Height: 12.8 cm
Requirement of label.
- Width: 12.5 cm
- Height: 11 cm
- Breeza Vita and Logo must not be changed. (W 3.5 cm x H 3 cm)
- Font: All detail must be black color. But each heading section such as Tips, Easy steps for use, Caution must be highlighted or in other notable color.
- The layout of label is flexible. However, we want Breeza Vita and logo on top of the can.
- Leave a little space below L' Breeza Vita logo then put “Jasmine Rose scent” with gold color highlighted
- Follow by “95% quality oxygen” and “Up to 45+ inhalations”
- At the bottom of bottle must be “4 liters of oxygen”
- Please design 4 vectors to put on the label. We need running or cardio exercise, drinking, recovery, altitude. The vectors given are samples only.
- We expected to have snowflake as theme color (glossy white) on label background. It could be falling snowflake, thick layer of snow on the ground, snow on mountains.
- Please leave some space for barcode.
Target Market(s)
Our target countries are USA and Europe. Those who exhausted from intense exercises, stress from work, hangover from drinking, or ever those caused by altitude.
Requirements
Must have
- Requirement of label.
- - Width: 12.5 cm
- - Height: 11 cm
- - Breeza Vita and Logo must not be changed. (W 3.5 cm x H 3 cm)
- - Font: All detail must be black color. But each heading section such as Tips, Easy steps for use, Caution must be highlighted or in other notable color.
- - The layout of label is flexible. However, we want L' Breeza Vita and logo on top of the can.
- - Leave a little space below L' Breeza Vita logo then put “Jasmine Rose scent” with gold color highlighted
- - Follow by “95% quality oxygen” and “Up to 45+ inhalations”
- - At the bottom of bottle must be “4 liters of oxygen”
- - Please design 4 vectors to put on the label. We need running or cardio exercise, drinking, recovery, altitude. The vectors given are samples only.
- - We expected to have snowflake as theme color (white) on label background. It could be falling snowflake, thick layer of snow on the ground, snow on mountains.
- - Please leave some space for barcode.
Nice to have
- We want our product to be very notable, classy, international, luxury look with glossy white color and clean+anti-fingerprints. Easy to read even though the font size is small.
Should not have
- cartoon design, not classy or luxury.

```html
<!DOCTYPE html>
<html lang="en">
<head>
<meta charset="utf-8">
<title>Breeza Vita – Oxygen Can Label</title>
<link rel="stylesheet" href="https://fonts.googleapis.com/css2?family=Open+Sans:wdth,wght@75..100,400..700&family=Quicksand:wght@400;500;700&display=swap">
<style>
  :root {
    --stage: #e8ebee;
    --sky-top: #b9e4fb;
    --sky-mid: #9fd6f6;
    --sky-low: #8cccf2;
    --snow: #ffffff;
    --snow-haze: rgba(255, 255, 255, 0.55);
    --ridge-blue: #7cc0ec;
    --ridge-pale: #d6ebf7;
    --ink: #111418;
    --heading: #1638d8;
    --gold-a: #c49a3f;
    --gold-b: #e3bd62;
    --gold-c: #b88c33;
  }
  * { box-sizing: border-box; margin: 0; padding: 0; }
  html, body { width: 1200px; height: 1200px; overflow: hidden; }
  body {
    background: radial-gradient(circle at 50% 40%, #f4f6f8 0%, var(--stage) 70%);
    position: relative;
    color: var(--ink);
  }
  .label {
    position: absolute;
    top: 272px;
    width: 298px;
    height: 654px;
    background: linear-gradient(180deg, var(--sky-top) 0%, var(--sky-mid) 55%, var(--sky-low) 80%);
    overflow: hidden;
    box-shadow: 0 6px 24px rgba(40, 60, 80, 0.12);
  }
  .label--front { left: 275px; }
  .label--back { left: 628px; }

  /* falling snow haze across the label */
  .snowfall {
    position: absolute;
    inset: 0 0 120px 0;
    background:
      radial-gradient(circle at 12% 16%, var(--snow-haze) 0, transparent 14%),
      radial-gradient(circle at 86% 10%, var(--snow-haze) 0, transparent 12%),
      radial-gradient(circle at 8% 62%, var(--snow-haze) 0, transparent 12%),
      radial-gradient(circle at 90% 52%, var(--snow-haze) 0, transparent 13%),
      radial-gradient(circle at 50% 88%, var(--snow-haze) 0, transparent 16%),
      radial-gradient(circle at 80% 84%, var(--snow-haze) 0, transparent 11%);
  }

  /* snowy ground band */
  .snowfield {
    position: absolute;
    left: 0; right: 0;
    top: 520px;
    height: 134px;
    background: linear-gradient(180deg, transparent 0%, var(--ridge-blue) 8%, var(--ridge-pale) 32%, var(--snow) 62%, var(--snow) 100%);
  }

  /* front */
  .brand {
    position: absolute;
    left: 0; right: 0;
    top: 44px;
    text-align: center;
    font-family: "Quicksand", sans-serif;
    font-weight: 700;
    color: var(--ink);
  }
  .brand__dot {
    display: block;
    width: 74px; height: 74px;
    margin: 0 auto 24px;
    border-radius: 50%;
    border: 3px solid var(--ink);
  }
  .brand__name { display: block; font-size: 36px; letter-spacing: 3px; line-height: 1; }
  .brand__sub { display: block; font-size: 15px; letter-spacing: 9px; margin-top: 6px; padding-left: 9px; }

  .scent-band {
    position: absolute;
    left: 6px; right: 10px;
    top: 234px;
    height: 50px;
    background: linear-gradient(180deg, var(--gold-b) 0%, var(--gold-a) 55%, var(--gold-c) 100%);
    display: flex; align-items: center; justify-content: center;
    font-family: "Quicksand", sans-serif;
    font-weight: 500;
    font-size: 25px;
    color: var(--ink);
  }
  .claims {
    position: absolute;
    left: 0; right: 0;
    top: 316px;
    text-align: center;
    font-family: "Quicksand", sans-serif;
    font-weight: 500;
    font-size: 15.5px;
    letter-spacing: 1px;
    line-height: 29px;
  }
  .uses {
    position: absolute;
    left: 0; right: 0;
    top: 404px;
    display: flex;
    justify-content: space-around;
    padding: 0 6px;
  }
  .use {
    width: 66px;
    text-align: center;
    font-family: "Open Sans", sans-serif;
    font-stretch: 85%;
    font-size: 10.5px;
    line-height: 13px;
  }
  .use__badge {
    display: block;
    width: 44px; height: 44px;
    margin: 0 auto 8px;
    border-radius: 50%;
    background: var(--snow);
  }
  .use--recovery { font-weight: 600; }
  .volume {
    position: absolute;
    left: 0; right: 0;
    top: 614px;
    text-align: center;
    font-family: "Quicksand", sans-serif;
    font-weight: 500;
    font-size: 16px;
    letter-spacing: 1.5px;
  }

  /* back */
  .copy {
    position: absolute;
    left: 10px; right: 6px;
    font-family: "Open Sans", sans-serif;
    font-stretch: 84%;
    font-size: 12.4px;
    line-height: 15.5px;
  }
  .copy h2 {
    font-size: 12.4px;
    font-weight: 600;
    color: var(--heading);
    margin-bottom: 3px;
  }
  .copy p { padding-left: 16px; text-align: justify; }
  .copy ol { list-style: none; }
  .copy--tips { top: 30px; }
  .copy--steps { top: 184px; }
  .copy--caution { top: 288px; }
  .copy--notice { top: 400px; }
  .copy--notice p { padding-left: 0; }

  .recycle {
    position: absolute;
    left: 234px; top: 466px;
    width: 24px; height: 24px;
  }
  .origin {
    position: absolute;
    left: 184px; top: 502px;
    font-family: "Open Sans", sans-serif;
    font-stretch: 84%;
    font-size: 11px;
  }
  .socials {
    position: absolute;
    left: 8px; top: 540px;
    width: 158px;
    display: flex; flex-direction: column; gap: 3px;
    font-family: "Open Sans", sans-serif;
    font-stretch: 84%;
    font-weight: 600;
    font-size: 10px;
    z-index: 1;
  }
  .social { display: flex; align-items: center; gap: 5px; }
  .social__dot { width: 11px; height: 11px; border-radius: 50%; background: var(--ink); }
  .barcode-space {
    position: absolute;
    left: 172px; top: 524px;
    width: 120px; height: 70px;
    background: var(--snow);
    border: 2px solid #c9ced3;
    z-index: 1;
  }
  .website {
    position: absolute;
    left: 0; right: 0;
    top: 614px;
    text-align: center;
    font-family: "Quicksand", sans-serif;
    font-weight: 500;
    font-size: 16px;
    letter-spacing: 0.5px;
  }
</style>
</head>
<body>

<section class="label label--front" aria-label="Front label">
  <div class="snowfall" role="img" aria-label="Falling glossy white snowflakes"></div>

  <div class="brand">
    <span class="brand__dot"></span>
    <span class="brand__name">BREEZA</span>
    <span class="brand__sub">VITA</span>
  </div>

  <div class="scent-band">Jasmine Rose scent</div>

  <div class="claims">
    <p>95% quality oxygen</p>
    <p>Up to 45+ inhalations</p>
  </div>

  <div class="uses">
    <div class="use"><span class="use__badge" role="img" aria-label="Runner icon"></span>Cardio<br>Exercises</div>
    <div class="use"><span class="use__badge" role="img" aria-label="Cocktail glass icon"></span>Drinking</div>
    <div class="use use--recovery">
      <svg class="use__badge" viewBox="0 0 44 44" role="img" aria-label="Recovery plus icon">
        <circle cx="22" cy="22" r="22" fill="#fff"/>
        <circle cx="22" cy="22" r="14" fill="none" stroke="#111418" stroke-width="4"/>
        <rect x="19.5" y="13" width="5" height="18" fill="#111418"/>
        <rect x="13" y="19.5" width="18" height="5" fill="#111418"/>
      </svg>Recovery</div>
    <div class="use"><span class="use__badge" role="img" aria-label="Mountain peak icon"></span>Altitude</div>
  </div>

  <div class="snowfield" role="img" aria-label="Snow-covered mountains"></div>
  <p class="volume">4 liters of oxygen</p>
</section>

<section class="label label--back" aria-label="Back label">
  <div class="snowfall" role="img" aria-label="Falling glossy white snowflakes"></div>

  <div class="copy copy--tips">
    <h2>Tips:</h2>
    <p>Our quality oxygen is best to use when exhausted from intense exercises, stressful work, or even hangover from a long night party. Deeply breathing our quality oxygen for 2 seconds per shot and repeat up to 5 times. Over breathing than suggestion would cause dizziness.</p>
  </div>

  <div class="copy copy--steps">
    <h2>Easy steps for use:</h2>
    <ol>
      <li>1. Open the lid.</li>
      <li>2. Place the cap close to mouth.</li>
      <li>3. Press the cap to activate quality oxygen and inhale simultaneously.</li>
    </ol>
  </div>

  <div class="copy copy--caution">
    <h2>Caution:</h2>
    <p>Non-flammable.<br>Pressurizing container, store at temperature less than 50 °C<br>Do not pierce or burn even empty.</p>
  </div>

  <div class="copy copy--notice">
    <p>This product is not certified by FDA. The purpose is not for curing or preventing any symptoms. This product is for refreshment purpose only. Please use as directed only.</p>
  </div>

  <span class="recycle" role="img" aria-label="Recycling symbol">
    <svg viewBox="0 0 24 24" width="24" height="24"><circle cx="12" cy="12" r="10" fill="none" stroke="#111418" stroke-width="2.5"/></svg>
  </span>
  <p class="origin">Made in Thailand</p>

  <div class="snowfield" role="img" aria-label="Snow-covered mountains"></div>

  <div class="socials">
    <span class="social"><span class="social__dot"></span>Friendwall</span>
    <span class="social"><span class="social__dot"></span>Photoline</span>
    <span class="social"><span class="social__dot"></span>Marketbay</span>
  </div>
  <div class="barcode-space" aria-label="Space reserved for barcode"></div>

  <p class="website">www.breezavitaair.com</p>
</section>

</body>
</html>
```